Ledger Ready Business Card

I need a business card designed around my logo (which was designed here on Sketch Yard!)

Target Market(s)

Professional Businesses

Industry/Entity Type

Business

Requirements
Must have
• Details that must be on the business card:

Harriet Vantos
Director
0491 263 358
harriet@ledgerready.com.au
www.ledgerready.com.au
PO Box 4471 Alder Heights Vic 3915

```html
<!DOCTYPE html>
<html lang="en">
<head>
<meta charset="utf-8">
<title>Ledger Ready Business Card</title>
<link rel="stylesheet" href="https://fonts.googleapis.com/css2?family=Questrial&family=Cinzel:wght@400;600&display=swap">
<style>
  :root {
    --brand-red: #c82128;
    --brand-red-text: #d4232a;
    --ink-grey: #3d3d3d;
    --paper: #ffffff;
    --backdrop: #ebe8e5;
  }
  * { margin: 0; padding: 0; box-sizing: border-box; }
  html, body { width: 1200px; height: 1000px; overflow: hidden; }
  body {
    background: var(--backdrop);
    position: relative;
    font-family: "Questrial", sans-serif;
  }
  .card {
    position: absolute;
    left: 295px;
    width: 610px;
    height: 330px;
    box-shadow: 0 6px 18px rgba(0,0,0,0.18);
  }
  .card--front { top: 140px; background: var(--brand-red); color: var(--paper); }
  .card--back { top: 530px; background: var(--paper); }

  .wordmark {
    display: flex;
    align-items: center;
    gap: 12px;
    white-space: nowrap;
  }
  .wordmark__dot { display: block; }
  .card--front .wordmark {
    position: absolute;
    top: 136px;
    left: 0; right: 0;
    justify-content: center;
    font-size: 40px;
    color: var(--paper);
    letter-spacing: 1px;
  }
  .card--front .wordmark__dot { width: 22px; height: 22px; background: var(--paper); }
  .card__url {
    position: absolute;
    bottom: 26px;
    left: 0; right: 0;
    text-align: center;
    font-family: "Cinzel", serif;
    font-weight: 600;
    font-size: 12px;
    letter-spacing: 0.5px;
  }

  .card--back .wordmark {
    position: absolute;
    top: 48px;
    right: 32px;
    font-size: 22px;
    color: var(--ink-grey);
    gap: 9px;
  }
  .card--back .wordmark__dot { width: 13px; height: 13px; background: var(--brand-red); }
  .holder {
    position: absolute;
    left: 41px;
    top: 138px;
  }
  .holder__name {
    font-size: 34px;
    color: var(--brand-red-text);
    line-height: 1;
  }
  .holder__role {
    font-size: 14px;
    color: var(--ink-grey);
    letter-spacing: 5.5px;
  }
  .contact {
    position: absolute;
    right: 32px;
    bottom: 26px;
    list-style: none;
    text-align: right;
    font-size: 13px;
    line-height: 21px;
    color: var(--brand-red-text);
  }
</style>
</head>
<body>
  <section class="card card--front" aria-label="Card front">
    <div class="wordmark"><span class="wordmark__dot"></span><span class="wordmark__name">LEDGER READY</span></div>
    <p class="card__url">WWW.LEDGERREADY.COM.AU</p>
  </section>

  <section class="card card--back" aria-label="Card back">
    <div class="wordmark"><span class="wordmark__dot"></span><span class="wordmark__name">LEDGER READY</span></div>
    <div class="holder">
      <p class="holder__name">Harriet Vantos</p>
      <p class="holder__role">DIRECTOR</p>
    </div>
    <ul class="contact">
      <li>0491 263 358</li>
      <li>harriet@ledgerready.com.au</li>
      <li>www.ledgerready.com.au</li>
      <li>PO Box 4471 Alder Heights Vic 3915</li>
    </ul>
  </section>
</body>
</html>
```